Dental FAQ/advert tri-fold for holistic family dentist

We are a dental clinic with a holistic emphasis. We are seeking new clients, mainly middle classed families. A tri-fold brochure that is both a useful dental FAQ to keep in the house and acts as an advertisement for our clinic. It will be mailed out. It needs to look clean, modern, somewhat minimalist, and I want it to follow the Orble design esthetic. website is willowcrestdentalcare.com
Updates

I just updated the pamphlet file with revised text! Thanks for the nice designs so far, keep em coming.

Target Market(s)

Young families. Upper middle classes.

Industry/Entity Type

Dental

Requirements
Must have
• Follows our logo and colours.

```html
<!DOCTYPE html>
<html lang="en">
<head>
<meta charset="utf-8">
<title>Willowcrest Dental Care – Tri-fold Brochure</title>
<link href="https://fonts.googleapis.com/css2?family=Open+Sans:wght@400;600;700&family=Comfortaa:wght@400;700&display=swap" rel="stylesheet">
<style>
  :root{
    --bg:#8c9196;
    --paper:#ffffff;
    --blue:#1f74c9;
    --blue-deep:#0b4d9c;
    --blue-light:#5aa6e8;
    --green:#3aa935;
    --green-dark:#23852a;
    --ink:#3a3a3a;
    --tint:#e6f1fb;
  }
  *{box-sizing:border-box;margin:0;padding:0}
  html,body{width:846px;height:1200px;overflow:hidden}
  body{background:var(--bg);font-family:"Open Sans",Arial,sans-serif;color:var(--ink);position:relative}
  .sheet{position:absolute;left:35px;width:776px;height:580px;background:var(--paper);display:grid;grid-template-columns:repeat(3,1fr);box-shadow:0 4px 14px rgba(0,0,0,.25);overflow:hidden}
  .sheet--outside{top:12px}
  .sheet--inside{top:608px}
  .panel{position:relative;overflow:hidden;border-right:1px solid #eef1f4}
  .panel:last-child{border-right:none}
  .swoosh{position:absolute;left:0;width:100%;pointer-events:none}
  .swoosh--bottom{bottom:0;height:70px}
  .swoosh--top{top:0;height:60px}
  .photo{position:absolute;left:0;top:0;width:100%;height:165px;background:linear-gradient(135deg,#7fa35a,#c9a17a 55%,#d84a6a);clip-path:ellipse(95% 100% at 20% 0%)}
  .photo--staff{background:linear-gradient(135deg,#cfd3d6,#c63a3a 55%,#2b2b2b)}
  .content{position:absolute;left:16px;right:16px;z-index:2}
  .faq{margin-bottom:8px}
  .faq h3{font-size:8.2px;font-weight:700;color:#fff;background:linear-gradient(90deg,var(--green-dark),var(--green) 70%,#7cc96f);padding:3px 8px;margin:0 -16px 4px -16px;border-radius:0 10px 10px 0;line-height:1.25}
  .faq p,.lead{font-size:7.6px;line-height:1.38;text-align:justify}
  .lead{margin-bottom:6px}
  .mascot{width:70px;height:62px;margin:6px 0 0 8px;border-radius:40% 40% 30% 30%;background:radial-gradient(circle at 40% 40%,#fff,#c8d3de);}
  .contact{text-align:right;font-size:7.8px;font-weight:700;color:var(--blue);line-height:1.45;margin-top:8px}
  .cover{background:linear-gradient(160deg,var(--blue-light) 0%,var(--blue) 40%,var(--blue-deep) 100%)}
  .brand{position:absolute;top:14px;left:50%;transform:translateX(-50%);background:#fff;padding:10px 14px;display:flex;align-items:center;gap:6px;box-shadow:0 2px 6px rgba(0,0,0,.25);white-space:nowrap}
  .brand__dot{width:12px;height:12px;border-radius:50%;background:var(--green)}
  .brand__name{font-size:11px;font-weight:700;color:var(--blue-deep)}
  .cover-title{position:absolute;top:88px;left:40px;color:#fff;font-family:"Comfortaa",Arial,sans-serif;line-height:1.02}
  .cover-title .t1{font-size:22px;font-weight:700;display:block}
  .cover-title .t2{font-size:15px;display:block;padding-left:10px}
  .cover-title .t3{font-size:20px;display:block}
  .cover-photo{position:absolute;left:0;right:0;top:190px;bottom:58px;background:linear-gradient(120deg,#f3dccd,#e8bfa8 60%,#c99886);clip-path:ellipse(110% 100% at 80% 100%)}
</style>
</head>
<body>

<!-- Outside of the brochure -->
<section class="sheet sheet--outside">
  <div class="panel">
    <div class="photo" role="img" aria-label="Photo of a smiling young family, mother, father and baby outdoors"></div>
    <div class="content" style="top:176px">
      <div class="faq">
        <h3>How can I manage my sensitive teeth?</h3>
        <p>Using a soft bristled toothbrush as well as desensitizing toothpaste is helpful, but many people still experience painful teeth sensitivity. We are pleased to offer effective laser desensitization, which is both gentle and painless. Other dental procedures that may help reduce sensitivity include using white fillings or applying dentin sealers to cover exposed root surfaces. Using a custom fit mouth guard to can also prevent further enamel wear.</p>
      </div>
      <div class="faq">
        <h3>Do I need to have my wisdom teeth removed?</h3>
        <p>While some people keep their wisdom teeth well into adulthood, wisdom teeth often do not grow in properly and need to be removed before a problem arises. This usually happens between the ages of 16-22. Our dentist will be able to assess your wisdom teeth and provide proper treatment.</p>
      </div>
      <div class="faq">
        <h3>What can cause a toothache?</h3>
        <p>Toothaches are caused by an irritated nerve within the tooth, or by an infection surrounding the tooth. Prior to your dental appointment an over the counter pain medication such as ibuprofen will usually provide temporary relief. At your visit, our dentist will determine the exact cause</p>
      </div>
    </div>
    <svg class="swoosh swoosh--bottom" viewBox="0 0 260 70" preserveAspectRatio="none" aria-hidden="true">
      <path d="M0 40 Q130 70 260 20 L260 70 L0 70Z" fill="#1f74c9"/>
      <path d="M0 50 Q130 72 260 34" fill="none" stroke="#fff" stroke-width="3"/>
    </svg>
  </div>

  <div class="panel">
    <div class="content" style="top:14px">
      <p class="lead">of the problem and provide treatment options.</p>
      <div class="faq">
        <h3>What should I do if I knock a tooth out?</h3>
        <p>Say sorry to the other person! Just kidding. If a tooth is knocked clean out, it can sometimes be re-implanted, if done within 30-60 minutes. Gently rinse the tooth off, and store it in a solution of milk or clean water and make your way to a dentist as soon as possible.</p>
      </div>
      <div class="faq">
        <h3>Should I wear a mouth guard during recreational activities?</h3>
        <p>Mouth guards should be used by anyone who plays contact sports such as hockey, football, boxing, soccer, basketball, and lacrosse. Your dentist can create a custom appliance that provides much more comfort and protection than a store-bought appliance.</p>
      </div>
      <div class="faq">
        <h3>What's the difference between teeth whitening in a dental office and store bought kits?</h3>
        <p>Our dental clinic can supply you with a custom fit tray to maximize your teeth whitening. Our dental office is able to prescribe stronger formulations of the whitening solution for a longer lasting, whiter smile.</p>
      </div>
      <div class="mascot" role="img" aria-label="Cartoon tooth character holding a toothbrush"></div>
      <div class="contact">
        Suite 210, 4415 Maple Ridge Way SE,<br>
        Calgary AB, T2X 4K9<br>
        Call us: (403) 555-0148<br>
        admin@willowcrestdentalcare.com
      </div>
    </div>
    <svg class="swoosh swoosh--bottom" viewBox="0 0 260 70" preserveAspectRatio="none" aria-hidden="true">
      <path d="M0 20 Q120 60 260 30 L260 70 L0 70Z" fill="#1f74c9"/>
      <path d="M0 32 Q120 68 260 42" fill="none" stroke="#fff" stroke-width="3"/>
    </svg>
  </div>

  <div class="panel cover">
    <div class="brand">
      <span class="brand__dot"></span>
      <span class="brand__name">Willowcrest Dental Care</span>
    </div>
    <h1 class="cover-title">
      <span class="t1">Dentistry</span>
      <span class="t2">for your</span>
      <span class="t3">Friends</span>
      <span class="t2">&amp; Family</span>
    </h1>
    <div class="cover-photo" role="img" aria-label="Close-up photo of a young woman flossing her teeth"></div>
    <svg class="swoosh" style="top:170px;height:50px" viewBox="0 0 260 50" preserveAspectRatio="none" aria-hidden="true">
      <path d="M0 50 Q60 10 260 30" fill="none" stroke="#fff" stroke-width="4"/>
    </svg>
  </div>
</section>

<!-- Inside of the brochure -->
<section class="sheet sheet--inside">
  <div class="panel">
    <div class="photo photo--staff" role="img" aria-label="Photo of three smiling dental staff members in uniform"></div>
    <div class="content" style="top:176px">
      <div class="faq">
        <h3>When should my child first start visiting the dentist?</h3>
        <p>The Prairie Dental Council recommends bringing your child to see a dentist within six months of their first tooth appearing. We recommend bringing your children in for short "happy visits" that build their confidence and comfort at the dental clinic. A happy visit is free, unless dental services are provided. Children can observe your appointments and they can learn the fun parts of the dental visit, such as counting and polishing teeth, and riding up and down in the dental chair. And of course, the best part, the prize drawer at the end of the appointment. We find that children who come for happy visits experience little to no dental fear or anxiety in their coming years.</p>
      </div>
      <div class="faq">
        <h3>How often should I get dental checkups and cleanings?</h3>
        <p>Everybody is different, and has different needs when it comes to regular examinations and cleanings. Most people need to have their teeth cleaned at least every 6 months. Those with gum disease present may require more frequent appointments.</p>
      </div>
    </div>
    <svg class="swoosh swoosh--bottom" viewBox="0 0 260 70" preserveAspectRatio="none" aria-hidden="true">
      <path d="M0 10 Q140 70 260 40 L260 70 L0 70Z" fill="#1f74c9"/>
      <path d="M0 24 Q140 76 260 52" fill="none" stroke="#fff" stroke-width="3"/>
    </svg>
  </div>

  <div class="panel">
    <div class="content" style="top:22px">
      <div class="faq">
        <h3>What is dental fluorosis?</h3>
        <p>Dental fluorosis is a change in the appearance of tooth enamel caused by too much fluoride while teeth are still forming. It usually shows as faint white lines or specks that often go unnoticed. Dental fluorosis is a change in the appearance of teeth, often causing small white specks to appear. It is caused when higher than optimal amounts of fluoride are ingested in early childhood. Fluoride-free options for dental care are available at our office.</p>
      </div>
      <div class="faq">
        <h3>Are amalgam fillings containing mercury safe?</h3>
        <p>Northland Health Agency's official position states that amalgams are safe, but should be avoided in certain people with medical conditions. It is best to consult with your dentist directly. Mercury-free options for dental care are available, and we offer a specific and safe method of mercury removal.</p>
      </div>
      <div class="faq">
        <h3>Do you offer options for anxious patients?</h3>
        <p>Yes. We take time to explain each step, offer gentle techniques and a calm, quiet room so every visit feels relaxed and comfortable.</p>
      </div>
    </div>
    <svg class="swoosh swoosh--bottom" viewBox="0 0 260 70" preserveAspectRatio="none" aria-hidden="true">
      <path d="M0 50 Q150 72 260 56 L260 70 L0 70Z" fill="#1f74c9"/>
    </svg>
  </div>

  <div class="panel">
    <svg class="swoosh swoosh--top" viewBox="0 0 260 60" preserveAspectRatio="none" aria-hidden="true">
      <path d="M0 0 L260 0 L260 50 Q150 0 0 14Z" fill="#1f74c9"/>
      <path d="M0 22 Q150 8 260 58" fill="none" stroke="#5aa6e8" stroke-width="3"/>
    </svg>
    <div class="content" style="top:62px">
      <div class="faq">
        <h3>What are dental sealants, and do they contain BPA?</h3>
        <p>Dental sealants are a way to protect a tooth from forming a cavity by sealing the natural pits and grooves in a tooth with resin. Some sealants do not contain Bis-phenol A, and you may ask your dentist if the type of material used has BPA.</p>
      </div>
      <div class="faq">
        <h3>What is gum disease and how can it affect my health?</h3>
        <p>Gum disease, or periodontal disease, is when bacteria and tartar on your teeth cause inflammation of the gums and the bone supporting your teeth. When severe enough, bone loss occurs, leading to loose teeth and gum abscesses. Gum disease can be treated by daily flossing and regular dental cleaning appointments. Our dentist and dental hygienists will be able to discuss treatment options available for you.</p>
      </div>
      <div class="faq">
        <h3>What do I do about bad breath?</h3>
        <p>80% of bad breath comes from an oral source. For instance, cavities, cracked fillings, gum disease, and less-than-clean dentures can all lead to bad breath. An examination by our dentist will discover the source of the problem, and frequent and thorough dental cleanings will often alleviate this embarrassing problem.</p>
      </div>
    </div>
    <svg class="swoosh swoosh--bottom" viewBox="0 0 260 70" preserveAspectRatio="none" aria-hidden="true">
      <path d="M0 56 Q120 72 260 50 L260 70 L0 70Z" fill="#1f74c9"/>
    </svg>
  </div>
</section>

</body>
</html>
```